Marketing collateral for the bilingual preschool
Kestrel Förskola AB Kestrel Preschool Ltd
Marketing collateral for the bilingual preschool - Childcare
Creative Brief
Childcare
Future customers-parents looking for a good preschool for their children.
Folder should be in a form of a template with possibility to change information when it will be needed. At the same time, all information needs to be presented in two languages, i.e. be bilingual. I'd like to have illustrations/photo presenting the preschool profile: bilingual, international, multicultural. I don't want our current preschool children's photos from our website will be used.

```html
<!DOCTYPE html>
<html lang="en">
<head>
<meta charset="utf-8">
<title>Kestrel Preschool – Marketing Collateral, English Version</title>
<link rel="stylesheet" href="https://fonts.googleapis.com/css2?family=Open+Sans:wght@400;600;800&family=Kaushan+Script&display=swap">
<style>
  :root{
    --board:#1f1f1f;
    --label:#d6d6d6;
    --lime:#8cc63e;
    --lime-light:#b7dc6c;
    --lime-dark:#4f8f1c;
    --grass:#3d8a22;
    --grass-light:#6fb52f;
    --cream:#fbf7dc;
    --paper:#fffef4;
    --orange:#f7941d;
    --red:#d7261e;
    --yellow:#ffd92e;
    --blue:#27aae1;
    --purple:#8e44ad;
    --ink:#24340f;
    --ink-soft:#3c4d22;
  }
  *{box-sizing:border-box;margin:0;padding:0}
  html,body{width:1200px;height:703px;overflow:hidden;background:var(--board)}
  body{position:relative;font-family:"Open Sans",Arial,sans-serif;color:var(--ink)}

  .board-title{position:absolute;top:22px;left:0;width:1200px;text-align:center;color:var(--label);font-size:13px}
  .section-label{position:absolute;color:var(--label);font-size:13px}

  .piece{position:absolute;overflow:hidden;background:linear-gradient(160deg,var(--lime-light),var(--lime) 55%,var(--lime-dark))}
  .panel{position:absolute;top:0;bottom:0}
  .fold{border-left:1px solid rgba(0,0,0,.15)}

  .grass{position:absolute;left:0;right:0;bottom:0;height:28px;
    background:linear-gradient(180deg,var(--grass-light),var(--grass))}

  .photo{position:absolute;border-radius:50%;border:4px solid var(--yellow);
    background:radial-gradient(circle at 40% 35%,#f3d2b3,#c99a6e 45%,#7fa7c9 80%)}
  .photo.red{border-color:var(--red)}
  .photo.blue{border-color:var(--blue)}
  .photo.purple{border-color:var(--purple)}
  .photo.room{background:radial-gradient(circle at 50% 40%,#f1e0c0,#c9a36c 55%,#8c6a3d)}
  .photo.kids{border:none;border-radius:40% 40% 0 0;background:radial-gradient(circle at 50% 30%,#f2c9a5,#d9874a 45%,#3f7fc4 85%)}

  .brand{position:absolute;z-index:2;display:flex;align-items:center;gap:4px;
    font-weight:800;color:var(--red);line-height:1.05;white-space:nowrap}
  .brand-dot{border-radius:50%;background:var(--orange);flex:none}
  .brand-name{display:block}

  .heading{position:absolute;font-family:"Kaushan Script",cursive;color:var(--orange);line-height:1.1;white-space:nowrap}
  .heading.red{color:var(--red)}
  .copy{position:absolute;font-size:6px;line-height:1.45;color:var(--ink)}
  .phone{position:absolute;font-family:"Kaushan Script",cursive;color:var(--orange);line-height:1;white-space:nowrap}
  .note{position:absolute;font-size:6px;font-weight:600;color:var(--red);white-space:nowrap}

  .addr-box{position:absolute;background:#fff;border:1px solid #c8d9a2}
  .addr-line{height:1px;background:#b8c99a;margin:9px 8px 0}
  .stamp{position:absolute;border:1px dashed var(--lime-dark)}
</style>
</head>
<body>

<div class="board-title">English Version</div>

<div class="section-label" style="left:118px;top:72px">Bi Fold Brochure</div>
<div class="section-label" style="left:610px;top:72px">Postcard</div>
<div class="section-label" style="left:985px;top:76px">Advertisement</div>
<div class="section-label" style="left:613px;top:352px">Flyer</div>

<!-- Bi-fold brochure, outside -->
<section class="piece brochure-outside" style="left:43px;top:96px;width:351px;height:221px">
  <div class="panel back-cover" style="left:0;width:175px;background:linear-gradient(160deg,var(--lime-light),var(--lime))">
    <div class="brand" style="left:40px;top:72px;font-size:11px"><span class="brand-dot" style="width:9px;height:9px"></span><span class="brand-name">Kestrel Preschool</span></div>
    <div class="copy" style="left:90px;top:100px">
      Kestrel Förskola AB<br>Kestrel Preschool Ltd<br>Parkvägen 12, Stockholm<br>Tel 08-555 01 42<br>info@kestrelpreschool.se
    </div>
  </div>
  <div class="panel front-cover fold" style="left:175px;width:176px">
    <div class="brand" style="left:10px;top:10px;font-size:11px"><span class="brand-dot" style="width:9px;height:9px"></span><span class="brand-name">Kestrel<br>Preschool</span></div>
    <div class="photo" role="img" aria-label="Photo of smiling children at play" style="left:60px;top:40px;width:106px;height:106px"></div>
    <div class="photo red room" role="img" aria-label="Photo of a bright preschool room" style="left:12px;top:96px;width:54px;height:54px"></div>
    <div class="photo blue" role="img" aria-label="Photo of a child drawing" style="left:124px;top:142px;width:40px;height:40px"></div>
  </div>
  <div class="grass" role="img" aria-label="Grass border with flowers"></div>
</section>

<!-- Postcard front -->
<section class="piece postcard-front" style="left:413px;top:96px;width:216px;height:221px">
  <div class="brand" style="left:10px;top:12px;font-size:12px"><span class="brand-dot" style="width:10px;height:10px"></span><span class="brand-name">Kestrel<br>Preschool</span></div>
  <div class="photo" role="img" aria-label="Photo of children smiling together" style="left:102px;top:6px;width:108px;height:108px"></div>
  <div class="photo red room" role="img" aria-label="Photo of a preschool classroom" style="left:48px;top:62px;width:54px;height:54px"></div>
  <div class="heading" style="left:12px;top:118px;font-size:12px">Welcome to our preschool</div>
  <div class="copy" style="left:12px;top:136px;width:190px">A bilingual, international and multicultural place to learn, play and grow together.</div>
  <div class="note" style="left:12px;top:160px">Call us today</div>
  <div class="phone" style="left:12px;top:170px;font-size:17px">08-555 01 42</div>
  <div class="grass" role="img" aria-label="Grass border with flowers"></div>
</section>

<!-- Postcard back -->
<section class="piece postcard-back" style="left:634px;top:96px;width:220px;height:221px;background:linear-gradient(160deg,#f4f7c8,var(--lime-light))">
  <div class="copy" style="left:10px;top:16px;font-weight:600">Kestrel Preschool Ltd</div>
  <div class="heading" style="left:10px;top:70px;font-size:11px">Opening hours</div>
  <div class="copy" style="left:10px;top:86px">Mon–Fri 7:00–18:00<br>Ages 1–5 years</div>
  <div style="position:absolute;left:108px;top:14px;bottom:40px;width:1px;background:var(--lime-dark)"></div>
  <div class="stamp" style="right:10px;top:12px;width:28px;height:32px"></div>
  <div class="addr-box" style="left:118px;top:60px;width:92px;height:70px">
    <div class="addr-line"></div><div class="addr-line"></div><div class="addr-line"></div><div class="addr-line"></div><div class="addr-line"></div>
  </div>
  <div class="grass" role="img" aria-label="Grass border with flowers"></div>
</section>

<!-- Advertisement -->
<section class="piece advertisement" style="left:907px;top:101px;width:240px;height:307px;background:linear-gradient(180deg,var(--paper),var(--cream) 45%,var(--lime) 45%,var(--lime-dark))">
  <div class="brand" style="left:12px;top:16px;font-size:13px"><span class="brand-dot" style="width:11px;height:11px"></span><span class="brand-name">Kestrel<br>Preschool</span></div>
  <div class="photo" role="img" aria-label="Photo of children playing with toys" style="left:106px;top:12px;width:126px;height:126px"></div>
  <div class="copy" style="left:12px;top:150px;width:140px;font-size:7px">Swedish and English every day in a warm, caring setting.</div>
  <div class="heading red" style="left:12px;top:190px;font-size:13px">Admissions open for autumn</div>
  <div class="note" style="left:12px;top:214px;font-size:7px">For more information call</div>
  <div class="phone" style="left:12px;top:228px;font-size:22px">08-555 01 42</div>
  <div class="photo kids" role="img" aria-label="Photo of a group of smiling children" style="left:150px;top:218px;width:88px;height:89px"></div>
</section>

<!-- Bi-fold brochure, inside -->
<section class="piece brochure-inside" style="left:43px;top:336px;width:351px;height:221px">
  <div class="panel" style="left:0;width:175px">
    <div class="photo purple" role="img" aria-label="Photo of a child reading" style="left:8px;top:68px;width:70px;height:70px"></div>
    <div class="heading" style="left:84px;top:18px;font-size:11px">Why choose us?</div>
    <div class="copy" style="left:84px;top:34px;width:84px">Small groups, qualified teachers and two languages from day one.</div>
  </div>
  <div class="panel fold" style="left:175px;width:176px">
    <div class="photo room" role="img" aria-label="Photo of a play area" style="left:8px;top:8px;width:62px;height:62px"></div>
    <div class="photo red" role="img" aria-label="Photo of children at a table" style="left:104px;top:20px;width:64px;height:64px"></div>
    <div class="heading" style="left:10px;top:80px;font-size:11px">Our profile</div>
    <div class="copy" style="left:10px;top:96px;width:90px">International friends, shared cultures and playful learning.</div>
    <div class="heading red" style="left:10px;top:136px;font-size:10px">Contact</div>
    <div class="photo kids" role="img" aria-label="Photo of smiling children" style="left:104px;top:140px;width:66px;height:60px"></div>
  </div>
  <div class="grass" role="img" aria-label="Grass border with flowers"></div>
</section>

<!-- Flyer front -->
<section class="piece flyer-front" style="left:413px;top:377px;width:216px;height:307px">
  <div class="brand" style="left:12px;top:12px;font-size:12px"><span class="brand-dot" style="width:10px;height:10px"></span><span class="brand-name">Kestrel<br>Preschool</span></div>
  <div class="photo" role="img" aria-label="Photo of children smiling together" style="left:98px;top:10px;width:112px;height:112px"></div>
  <div class="photo red room" role="img" aria-label="Photo of a bright classroom" style="left:14px;top:48px;width:72px;height:72px"></div>
  <div class="photo blue" role="img" aria-label="Photo of a child painting" style="left:80px;top:104px;width:40px;height:40px"></div>
  <div class="heading" style="left:12px;top:154px;font-size:13px">Welcome to our preschool</div>
  <div class="copy" style="left:12px;top:174px;width:190px">We help children grow with confidence in Swedish and English.</div>
  <div class="note" style="left:12px;top:216px">For more information call</div>
  <div class="phone" style="left:12px;top:228px;font-size:20px">08-555 01 42</div>
  <div class="grass" role="img" aria-label="Grass border with flowers"></div>
</section>

<!-- Flyer back -->
<section class="piece flyer-back" style="left:638px;top:377px;width:216px;height:307px">
  <div class="photo room" role="img" aria-label="Photo of a preschool play corner" style="left:8px;top:10px;width:96px;height:96px;border-radius:12px"></div>
  <div class="heading" style="left:114px;top:14px;font-size:11px">What we offer</div>
  <div class="copy" style="left:114px;top:30px;width:94px">Music, art, outdoor play and healthy meals every day.</div>
  <div class="heading" style="left:114px;top:76px;font-size:11px">Preschool values</div>
  <div class="copy" style="left:114px;top:92px;width:94px">Respect, curiosity and joy in learning.</div>
  <div class="heading red" style="left:12px;top:128px;font-size:11px">Opening hours</div>
  <div class="copy" style="left:12px;top:144px">Mon–Fri 7:00–18:00</div>
  <div class="photo red" role="img" aria-label="Photo of smiling children" style="left:120px;top:180px;width:88px;height:88px"></div>
  <div class="grass" role="img" aria-label="Grass border with flowers"></div>
</section>

</body>
</html>
```